Target Avatar Profile for Lead Generation

We are a marketing agency that does 'Persona Profiling' on behalf of our customers.
[1] I want to systemise the capture of 'Personas' for lead generation messaging by completing lots of questions about the targets - their likes, dislikes, pains, challenges and goals.
I am attaching a document where we have captured all the relevant information but I need this put into a better format - possibly an editable PDF?
[2]I am including an example of where we have tried to summarise it. Although I am not happy with the result, it gives you an idea of the process.
Ideally these A4 representations of the Avatar should be easily changed for different industries/customers depending on who they are targeting. If we can have a solid design that colour(s) is easily changed depending on the customer branding.
The current example is too light on graphics.
If you can imagine this A4 scaled to A3/A1 and printed out, framed and put on their walls in their office. It should be an engaging representation of an individual come to life.

So there is 2 things here - a data input form (A4) which I could access through a URL on our website, and an associated output (A4).

Target Market(s)

ICT Sector

Industry/Entity Type

Digital Marketing Agency

Requirements
Must have
• Clear, concise, engaging
Nice to have
• Ability to change base colours easily per customer

```html
<!DOCTYPE html>
<html lang="en">
<head>
<meta charset="utf-8">
<title>Persona Profile – Alasdair Brock</title>
<link rel="stylesheet" href="https://fonts.googleapis.com/css2?family=Montserrat:wght@700;800;900&family=Lato:wght@400;700&display=swap">
<style>
  :root{
    --brand:#345ea4;
    --brand-dark:#22407a;
    --side:#58595b;
    --ink:#231f20;
    --text:#3a3a3c;
    --panel:#f1f1f2;
    --ok:#27a74a;
    --bad:#e0232f;
    --white:#ffffff;
  }
  *{margin:0;padding:0;box-sizing:border-box}
  html,body{width:848px;height:1200px;overflow:hidden;background:var(--white)}
  body{position:relative;font-family:"Lato",Arial,sans-serif;color:var(--text)}
  .abs{position:absolute}

  /* sidebar */
  .sidebar{left:26px;top:30px;width:248px;height:1170px;background:var(--side);border-radius:124px 124px 0 0}
  .portrait{left:43px;top:47px;width:212px;height:212px;border-radius:50%;background:radial-gradient(circle at 50% 40%,#c9b3a4 0,#a48a7c 28%,#9db8e0 52%,#9bb6de 100%)}
  .band{left:0;width:298px;height:43px;background:var(--brand);display:flex;align-items:center;padding-left:85px;
        font-family:"Montserrat",Arial,sans-serif;font-weight:900;font-size:19px;color:var(--white);letter-spacing:.3px}
  .band-icon{position:absolute;left:43px;top:8px;width:28px;height:28px}
  .fold{left:274px;width:24px;height:12px}
  .feature{left:45px;display:flex;align-items:center;gap:10px;font-family:"Lato",Arial,sans-serif;font-weight:700;
           font-size:15.5px;color:var(--white);text-transform:uppercase}
  .feature .dot{width:30px;height:30px;border-radius:50%;background:var(--white);display:flex;align-items:center;justify-content:center}
  .about{left:48px;top:620px;list-style:none;color:var(--white);font-size:14px;line-height:24.9px}
  .about li::before{content:"";display:inline-block;width:5px;height:5px;border-radius:50%;background:var(--white);margin:0 10px 2px 0;vertical-align:middle}
  .hobby{left:73px;color:var(--white);font-size:14px}
  .hobby-rule{left:63px;height:2px;background:var(--white)}

  /* header */
  .name{left:330px;top:76px;font-family:"Montserrat",Arial,sans-serif;font-weight:900;font-size:50px;line-height:1;color:var(--ink);letter-spacing:-.5px;white-space:nowrap}
  .name .first{color:var(--brand)}
  .role{left:343px;top:127px;width:462px;font-family:"Montserrat",Arial,sans-serif;font-weight:700;font-size:11px;color:var(--text);
        display:flex;justify-content:space-between}
  .label{font-family:"Lato",Arial,sans-serif;font-weight:700;font-size:15px;color:var(--brand)}
  .value{font-size:15px;color:var(--text)}
  .rule{left:342px;top:195px;width:463px;height:1px;background:#9bb0d4}

  /* sections */
  .heading{left:384px;top:308px;font-family:"Montserrat",Arial,sans-serif;font-weight:900;font-size:25px;color:var(--ink)}
  .goal{left:350px;display:flex;align-items:center;gap:14px;font-size:15.5px;color:var(--text)}
  .panel{left:329px;width:519px;background:var(--panel)}
  .tab{left:329px;height:39px;background:var(--brand);display:flex;align-items:center;padding-left:60px;
       font-family:"Montserrat",Arial,sans-serif;font-weight:900;font-size:19px;color:var(--white)}
  .tab svg{position:absolute;left:17px;top:6px}
  .item{left:355px;display:flex;align-items:center;gap:14px;font-size:14px;color:var(--text)}
  .mark{width:19px;height:19px;flex:none}
</style>
</head>
<body>

<!-- sidebar -->
<div class="abs sidebar"></div>
<div class="abs portrait" role="img" aria-label="Portrait photo of the persona"></div>

<div class="abs band" style="top:299px">
  <svg class="band-icon" viewBox="0 0 28 28" fill="none" stroke="#fff" stroke-width="2"><circle cx="14" cy="11" r="9"/><circle cx="14" cy="9" r="3.5"/><path d="M8 16c2-3 10-3 12 0M8 19l-3 7 4-1 2 3 3-7M20 19l3 7-4-1-2 3-3-7"/></svg>
  KEY FEATURES
</div>
<svg class="abs fold" style="top:342px" viewBox="0 0 24 12"><polygon points="0,0 24,0 0,12" fill="var(--brand-dark)"/></svg>

<div class="abs feature" style="top:363px"><span class="dot"><svg width="16" height="16" viewBox="0 0 16 16" fill="var(--side)"><path d="M8 1a6 6 0 0 0-6 6c0 2 1 3 2 4v4h6v-2h2v-3l2-1-1-3a6 6 0 0 0-5-5z"/></svg></span>Pragmatic</div>
<div class="abs feature" style="top:400px"><span class="dot"><svg width="16" height="16" viewBox="0 0 16 16" fill="none" stroke="var(--side)" stroke-width="1.8"><path d="M1 7l4-3 3 2 3-2 4 3-6 6z"/></svg></span>Relationship Driven</div>
<div class="abs feature" style="top:437px"><span class="dot"><svg width="16" height="16" viewBox="0 0 16 16" fill="var(--side)"><path d="M8 13L3 8a3 3 0 0 1 5-4 3 3 0 0 1 5 4z"/></svg></span>Loyal</div>
<div class="abs feature" style="top:475px"><span class="dot"><svg width="18" height="16" viewBox="0 0 18 16" fill="none" stroke="var(--side)" stroke-width="1.6"><circle cx="4" cy="3" r="1.6" fill="var(--side)"/><path d="M4 6v8M8 3v10M10.5 3v10M13 8h4M15 6l-2 2 2 2"/></svg></span>Resilient</div>

<div class="abs band" style="top:558px">
  <svg class="band-icon" viewBox="0 0 28 28" fill="#fff"><circle cx="14" cy="8" r="6"/><path d="M3 27c0-8 4-12 11-12s11 4 11 12z"/></svg>
  ABOUT ME
</div>
<svg class="abs fold" style="top:601px" viewBox="0 0 24 12"><polygon points="0,0 24,0 0,12" fill="var(--brand-dark)"/></svg>

<ul class="abs about">
  <li>Family-Oriented Legacy Builder</li>
  <li>Community-Focused</li>
  <li>Hands-On Leader</li>
  <li>Reputation-Driven</li>
  <li>Practical &amp; Cautious</li>
  <li>Enjoys Outdoor Hobbies</li>
  <li>Values Hard Work &amp; Loyalty</li>
  <li>Community Involvement</li>
  <li>Proud &amp; Resilient</li>
  <li>Cautious with Change</li>
</ul>

<div class="abs band" style="top:919px">
  <svg class="band-icon" viewBox="0 0 28 28" fill="#fff"><circle cx="6" cy="15" r="4"/><circle cx="20" cy="17" r="4"/><path d="M13 3l3 5-3 5-3-5zM14 28c0-5 2-7 6-7s6 2 6 7zM0 25c0-3 2-5 5-5v5z"/></svg>
  HOBBIES
</div>
<svg class="abs fold" style="top:961px" viewBox="0 0 24 12"><polygon points="0,0 24,0 0,12" fill="var(--brand-dark)"/></svg>

<svg class="abs" style="left:52px;top:988px" width="12" height="190" viewBox="0 0 12 190"><path d="M10 2C4 8 4 14 4 20v150c0 8 2 12 6 16" stroke="#fff" stroke-width="4" fill="none"/></svg>
<div class="abs hobby" style="top:986px;left:75px">Writing</div>
<div class="abs hobby-rule" style="top:1008px;width:103px"></div>
<div class="abs hobby" style="top:1017px">Reading Books</div>
<div class="abs hobby-rule" style="top:1041px;width:163px"></div>
<div class="abs hobby" style="top:1048px">Playing Football</div>
<div class="abs hobby-rule" style="top:1071px;width:181px"></div>
<div class="abs hobby" style="top:1079px">Photography</div>
<div class="abs hobby-rule" style="top:1100px;width:147px"></div>
<div class="abs hobby" style="top:1108px;left:75px">Traveling</div>

<!-- header -->
<div class="abs name"><span class="first">ALASDAIR</span> BROCK</div>
<div class="abs role"><span>C</span><span>H</span><span>I</span><span>E</span><span>F</span><span>&nbsp;</span><span>E</span><span>X</span><span>E</span><span>C</span><span>U</span><span>T</span><span>I</span><span>V</span><span>E</span><span>&nbsp;</span><span>O</span><span>F</span><span>F</span><span>I</span><span>C</span><span>E</span><span>R</span></div>

<span class="abs label" style="left:342px;top:170px">Gender:</span><span class="abs value" style="left:423px;top:170px">Male</span>
<span class="abs label" style="left:504px;top:170px">Location:</span><span class="abs value" style="left:587px;top:170px">Scotland</span>
<div class="abs rule"></div>
<span class="abs label" style="left:342px;top:198px">Age:</span><span class="abs value" style="left:423px;top:198px">50</span>
<span class="abs label" style="left:504px;top:198px">Industry:</span><span class="abs value" style="left:587px;top:198px">Construction</span>

<!-- priorities -->
<svg class="abs" style="left:349px;top:312px" width="25" height="22" viewBox="0 0 25 22" fill="var(--brand)"><circle cx="6" cy="5" r="3"/><path d="M1 18v-6c0-2 2-4 5-4s5 2 5 4v6z"/><path d="M14 3h3M14 10h3M14 17h3M19 2l1.5 1.5L23 1M19 9l1.5 1.5L23 8M19 16l1.5 1.5L23 15" stroke="var(--brand)" stroke-width="1.3" fill="none"/></svg>
<div class="abs heading">PRIORITIES &amp; GOALS</div>

<div class="abs goal" style="top:361px"><svg class="mark" viewBox="0 0 20 20" fill="none" stroke="var(--brand)" stroke-width="1.5"><circle cx="9" cy="11" r="8"/><circle cx="9" cy="11" r="5"/><circle cx="9" cy="11" r="2"/><path d="M9 11l8-8M14 3h3v3"/></svg>Protect business legacy &amp; ensure sustainability.</div>
<div class="abs goal" style="top:398px"><svg class="mark" viewBox="0 0 20 20" fill="none" stroke="var(--brand)" stroke-width="1.5"><circle cx="9" cy="11" r="8"/><circle cx="9" cy="11" r="5"/><circle cx="9" cy="11" r="2"/><path d="M9 11l8-8M14 3h3v3"/></svg>Boost profitability by reducing costs and inefficiencies.</div>
<div class="abs goal" style="top:436px"><svg class="mark" viewBox="0 0 20 20" fill="none" stroke="var(--brand)" stroke-width="1.5"><circle cx="9" cy="11" r="8"/><circle cx="9" cy="11" r="5"/><circle cx="9" cy="11" r="2"/><path d="M9 11l8-8M14 3h3v3"/></svg>Maintain trust with clients &amp; residents.</div>
<div class="abs goal" style="top:473px"><svg class="mark" viewBox="0 0 20 20" fill="none" stroke="var(--brand)" stroke-width="1.5"><circle cx="9" cy="11" r="8"/><circle cx="9" cy="11" r="5"/><circle cx="9" cy="11" r="2"/><path d="M9 11l8-8M14 3h3v3"/></svg>Adopt digital tools to streamline workflows and manage risks.</div>
<div class="abs goal" style="top:511px"><svg class="mark" viewBox="0 0 20 20" fill="none" stroke="var(--brand)" stroke-width="1.5"><circle cx="9" cy="11" r="8"/><circle cx="9" cy="11" r="5"/><circle cx="9" cy="11" r="2"/><path d="M9 11l8-8M14 3h3v3"/></svg>Empower his team to drive growth and stay competitive.</div>

<!-- motivations -->
<div class="abs panel" style="top:579px;height:272px"></div>
<div class="abs tab" style="top:560px;width:222px">
  <svg width="32" height="26" viewBox="0 0 32 26" fill="#fff"><rect x="9" y="9" width="14" height="12" rx="4"/><rect x="12" y="20" width="8" height="5"/><path d="M16 0v4M8 3l2 3M24 3l-2 3M3 12h4M25 12h4" stroke="#fff" stroke-width="1.4"/></svg>
  MOTIVATIONS
</div>
<div class="abs item" style="top:621px"><svg class="mark" viewBox="0 0 20 20"><circle cx="10" cy="10" r="9.5" fill="var(--ok)"/><path d="M5.5 10.5l3 3 6-6" stroke="#fff" stroke-width="2.2" fill="none"/></svg>Protect Legacy: Ensure long-term profitability and resilience.</div>
<div class="abs item" style="top:658px"><svg class="mark" viewBox="0 0 20 20"><circle cx="10" cy="10" r="9.5" fill="var(--ok)"/><path d="M5.5 10.5l3 3 6-6" stroke="#fff" stroke-width="2.2" fill="none"/></svg>Deliver Quality: Build trust with clients and residents.</div>
<div class="abs item" style="top:696px"><svg class="mark" viewBox="0 0 20 20"><circle cx="10" cy="10" r="9.5" fill="var(--ok)"/><path d="M5.5 10.5l3 3 6-6" stroke="#fff" stroke-width="2.2" fill="none"/></svg>Stay Competitive: Reduce inefficiencies with smart solutions.</div>
<div class="abs item" style="top:733px"><svg class="mark" viewBox="0 0 20 20"><circle cx="10" cy="10" r="9.5" fill="var(--ok)"/><path d="M5.5 10.5l3 3 6-6" stroke="#fff" stroke-width="2.2" fill="none"/></svg>Manage Risks: Simplify compliance and minimise challenges.</div>
<div class="abs item" style="top:770px"><svg class="mark" viewBox="0 0 20 20"><circle cx="10" cy="10" r="9.5" fill="var(--ok)"/><path d="M5.5 10.5l3 3 6-6" stroke="#fff" stroke-width="2.2" fill="none"/></svg>Support Team: Empower staff and foster stability.</div>
<div class="abs item" style="top:808px"><svg class="mark" viewBox="0 0 20 20"><circle cx="10" cy="10" r="9.5" fill="var(--ok)"/><path d="M5.5 10.5l3 3 6-6" stroke="#fff" stroke-width="2.2" fill="none"/></svg>Enhance Reputation: Meet demands and strengthen market position.</div>

<!-- frustrations -->
<div class="abs panel" style="top:902px;height:269px"></div>
<div class="abs tab" style="top:884px;width:233px">
  <svg width="32" height="28" viewBox="0 0 32 28" fill="none" stroke="#fff" stroke-width="1.5"><circle cx="16" cy="11" r="5"/><path d="M5 27c0-7 5-10 11-10s11 3 11 10zM10 20l6 5 6-5M3 3l3 2M29 3l-3 2M8 1l1 3M24 1l-1 3"/></svg>
  FRUSTRATIONS
</div>
<div class="abs item" style="top:949px"><svg class="mark" viewBox="0 0 20 20"><circle cx="10" cy="10" r="9.5" fill="var(--bad)"/><path d="M6.5 6.5l7 7M13.5 6.5l-7 7" stroke="#fff" stroke-width="2.2"/></svg>Manual Bottlenecks: Paperwork slows progress.</div>
<div class="abs item" style="top:986px"><svg class="mark" viewBox="0 0 20 20"><circle cx="10" cy="10" r="9.5" fill="var(--bad)"/><path d="M6.5 6.5l7 7M13.5 6.5l-7 7" stroke="#fff" stroke-width="2.2"/></svg>Tender Delays: Lengthy processes stall projects.</div>
<div class="abs item" style="top:1024px"><svg class="mark" viewBox="0 0 20 20"><circle cx="10" cy="10" r="9.5" fill="var(--bad)"/><path d="M6.5 6.5l7 7M13.5 6.5l-7 7" stroke="#fff" stroke-width="2.2"/></svg>Material Issues: Shortages increase costs.</div>
<div class="abs item" style="top:1061px"><svg class="mark" viewBox="0 0 20 20"><circle cx="10" cy="10" r="9.5" fill="var(--bad)"/><path d="M6.5 6.5l7 7M13.5 6.5l-7 7" stroke="#fff" stroke-width="2.2"/></svg>Lack of Visibility: Projects lack clarity.</div>
<div class="abs item" style="top:1098px"><svg class="mark" viewBox="0 0 20 20"><circle cx="10" cy="10" r="9.5" fill="var(--bad)"/><path d="M6.5 6.5l7 7M13.5 6.5l-7 7" stroke="#fff" stroke-width="2.2"/></svg>Regulatory Strain: Compliance is burdensome.</div>
<div class="abs item" style="top:1136px"><svg class="mark" viewBox="0 0 20 20"><circle cx="10" cy="10" r="9.5" fill="var(--bad)"/><path d="M6.5 6.5l7 7M13.5 6.5l-7 7" stroke="#fff" stroke-width="2.2"/></svg>Reactive Work: Limited focus on growth.</div>

</body>
</html>
```